Golden Coat All-Purpose Breading Bag Design

Our client, Harlow Food Products, is looking to re-design the packaging for their product, Pellworth's Golden Coat. Goldn Coat is an all-purpose food breading mix.

Harlow Foods has a registered trademark for this product, but they have not been using it for this particular 10 pound bag. They want to get the trademark onto the bag and also give the bag an updated look. They would like to continue to use the same red and blue colors. This 10 pound bag is not available on store shelves; it is sold to food service distributors who sell to restaurants.

All of the copy on the existing bag is still relevant, so we will want to incoprporate it into the bag design. Once these bags are filled with product, the tops get folded over about 1 inch and then sewn shut with thread.

Eventually, we will need the design applied to the Bag Template file attached, but that isn't important until a design is selected.

Target Market(s)

Restaurants

Industry/Entity Type

Food Manufacturing

Colors
0054AA
0677BA
7BADD7
CADEEF
E8F1F8
EB3D1F
EC4F4E
F09395
F8D3D4
FCEDEE

Requirements
Must have
• Trademark introduced to the design

```html
<!DOCTYPE html>
<html lang="en">
<head>
<meta charset="utf-8">
<title>Pellworth's Golden Coat – 10 lb Bag Template</title>
<link rel="stylesheet" href="https://fonts.googleapis.com/css2?family=Open+Sans:wght@400;600;700;800&display=swap">
<style>
  :root {
    --navy: #262262;
    --red: #a51e22;
    --white: #ffffff;
    --guide: #29abe2;
    --dieline: #ec008c;
    --ink: #1a1a1a;
    --crumb-light: #f0a640;
    --crumb-dark: #b5561a;
  }
  * { box-sizing: border-box; margin: 0; padding: 0; }
  html, body { width: 1200px; height: 912px; overflow: hidden; background: var(--white); }
  body { font-family: "Open Sans", Arial, sans-serif; color: var(--navy); }
  .bag-template { position: relative; width: 1200px; height: 912px; overflow: hidden; }
  .template-art { position: absolute; inset: 0; }
  .abs { position: absolute; }

  .tab { background: var(--navy); border-radius: 0 0 16px 16px; color: var(--white);
         display: flex; flex-direction: column; align-items: center; justify-content: flex-end; text-align: center; }
  .tab-side { left: 82px; top: 8px; width: 141px; height: 189px; padding-bottom: 22px; }
  .tab-side.back { left: 634px; }
  .tab-front { left: 298px; top: 8px; width: 261px; height: 270px; padding-bottom: 40px; }

  .brand-small { font-weight: 700; font-size: 17px; letter-spacing: .5px; }
  .brand-product { font-weight: 800; line-height: .95; }
  .tab-front .brand-small { font-size: 15px; margin-bottom: 8px; }
  .tab-front .brand-product { font-size: 46px; }

  .side-product { color: var(--red); text-align: center; width: 141px; font-size: 34px; top: 226px; }
  .side-product.left { left: 82px; }
  .side-product.back { left: 634px; }

  .front-brand { left: 830px; top: 100px; width: 310px; }
  .front-brand .brand-small { color: var(--navy); font-size: 24px; }
  .front-brand .brand-product { color: var(--red); font-size: 78px; margin-top: 6px; }

  .maker { left: 830px; top: 370px; width: 300px; text-align: center; color: var(--ink); }
  .maker strong { display: block; font-size: 11px; font-weight: 700; }
  .maker span { display: block; font-size: 8.5px; font-weight: 600; line-height: 1.25; }

  .chicken-photo { left: 264px; top: 268px; width: 280px; height: 200px;
                   background: radial-gradient(ellipse at 50% 50%, var(--crumb-light) 0%, #dc8530 55%, var(--crumb-dark) 80%, rgba(181,86,26,0) 100%);
                   border-radius: 45% 55% 40% 50%; }

  .about-copy { left: 77px; top: 466px; width: 146px; color: var(--white); font-size: 10.5px; line-height: 1.3;
                text-align: justify; font-weight: 600; }
  .about-copy p + p { margin-top: 14px; }

  .use-heading { left: 298px; top: 470px; width: 261px; text-align: center; color: var(--white); font-weight: 700; line-height: 1; }
  .use-heading .small { font-size: 16px; }
  .use-heading .big { font-size: 34px; font-weight: 800; }
  .use-heading .note { font-size: 8px; font-weight: 600; margin-top: 2px; }

  .food-list { left: 270px; top: 588px; width: 318px; height: 66px; background: var(--red); border-radius: 10px;
               color: var(--white); font-weight: 700; font-size: 12.5px; line-height: 1.45; text-align: center; padding-top: 4px; }
  .lot-box { left: 388px; top: 661px; width: 82px; height: 39px; background: var(--white); }

  .noting-heading { left: 626px; top: 458px; width: 158px; text-align: center; color: var(--white); font-weight: 800; font-size: 31px; line-height: 1.05; }
  .directions { left: 626px; top: 544px; width: 158px; color: var(--white); font-size: 12.6px; line-height: 1.27;
                text-align: justify; text-align-last: justify; font-weight: 600; }

  .front-copy { left: 801px; top: 484px; width: 360px; text-align: center; color: var(--white); }
  .front-copy h2 { font-size: 19px; font-weight: 800; }
  .front-copy .tag { font-size: 8.8px; font-weight: 600; margin-top: 6px; }
  .front-copy .tag + .tag { margin-top: 5px; }
  .front-copy .slogan { font-size: 16.5px; font-weight: 700; line-height: 1.25; margin-top: 22px; }

  .ingredients-band { left: 801px; top: 623px; width: 360px; height: 95px; background: var(--red); color: var(--white); text-align: center; padding-top: 14px; }
  .ingredients-band p { font-size: 8.8px; font-weight: 700; line-height: 1.35; }
  .ingredients-band .net { font-size: 19px; font-weight: 800; margin-top: 14px; }

  .bottom-slogan { left: 298px; top: 734px; width: 262px; height: 132px; border: 1.5px solid var(--guide);
                   display: flex; align-items: center; justify-content: center; text-align: center;
                   font-size: 10px; font-weight: 700; line-height: 1.35; }

  .color-bar { left: 596px; top: 780px; font-size: 5px; color: var(--ink); }
  .swatch-row { display: flex; gap: 3px; margin-bottom: 2px; }
  .swatch { display: flex; align-items: center; gap: 2px; width: 30px; }
  .swatch i { display: block; width: 9px; height: 8px; }
  .job-code { position: absolute; left: 84px; top: 26px; font-size: 5px; }

  .spec { left: 852px; top: 780px; color: var(--ink); font-size: 14px; line-height: 1.45; }
</style>
</head>
<body>
<main class="bag-template">
  <svg class="template-art" width="1200" height="912" viewBox="0 0 1200 912" aria-hidden="true">
    <g stroke="var(--guide)" stroke-width=".8" stroke-dasharray="3 3" fill="none">
      <line x1="0" y1="8" x2="1200" y2="8"/>
      <line x1="0" y1="370" x2="1200" y2="370"/>
      <line x1="50" y1="0" x2="50" y2="760"/>
      <line x1="56" y1="0" x2="56" y2="760"/>
      <line x1="153" y1="100" x2="153" y2="430"/>
      <line x1="248" y1="0" x2="248" y2="760"/>
      <line x1="256" y1="0" x2="256" y2="760"/>
      <line x1="428" y1="280" x2="428" y2="900"/>
      <line x1="602" y1="0" x2="602" y2="760"/>
      <line x1="610" y1="0" x2="610" y2="760"/>
      <line x1="705" y1="100" x2="705" y2="430"/>
      <line x1="800" y1="0" x2="800" y2="760"/>
      <line x1="808" y1="0" x2="808" y2="760"/>
      <line x1="1154" y1="0" x2="1154" y2="760"/>
      <line x1="40" y1="752" x2="586" y2="752"/>
      <line x1="840" y1="742" x2="1150" y2="742"/>
    </g>
    <g stroke="var(--guide)" stroke-width="1" fill="none">
      <rect x="70" y="106" width="166" height="326"/>
      <rect x="262" y="106" width="334" height="326"/>
      <rect x="622" y="106" width="166" height="326"/>
      <rect x="819" y="106" width="323" height="326"/>
    </g>
    <path d="M38,32 H1161 V766 H850 V754 H586 V890 H272 V766 H38 Z" fill="none" stroke="var(--dieline)" stroke-width="1.5"/>
    <path d="M50,430 C250,440 450,446 540,412 L608,387 C760,442 920,446 1161,383 V718 H50 Z" fill="var(--navy)"/>
    <path d="M50,430 C250,440 450,446 540,412 L608,387 C760,442 920,446 1161,383" fill="none" stroke="var(--red)" stroke-width="4"/>
    <g stroke="var(--ink)" stroke-width=".6">
      <line x1="30" y1="370" x2="38" y2="370"/><line x1="1161" y1="370" x2="1169" y2="370"/>
      <line x1="428" y1="890" x2="428" y2="898"/>
    </g>
  </svg>

  <div class="abs tab tab-side left">
    <span class="brand-small">Pellworth's</span>
  </div>
  <div class="abs brand-product side-product left">Golden<br>Coat</div>

  <div class="abs tab tab-front">
    <span class="brand-small">Pellworth's</span>
    <span class="brand-product">Golden<br>Coat</span>
  </div>

  <div class="abs tab tab-side back">
    <span class="brand-small">Pellworth's</span>
  </div>
  <div class="abs brand-product side-product back">Golden<br>Coat</div>

  <div class="abs front-brand">
    <div class="brand-small">Pellworth's</div>
    <div class="brand-product">Golden<br>Coat</div>
  </div>

  <div class="abs maker">
    <strong>By HARLOW FOOD PRODUCTS</strong>
    <span>418 MEADOW LANE</span>
    <span>CEDAR FALLS, IOWA 50613</span>
  </div>

  <div class="abs chicken-photo" role="img" aria-label="Photo of golden crispy fried chicken pieces"></div>

  <div class="abs about-copy">
    <p>Golden Coat is a prepared formula of pure foods that enables you to fry chicken from the raw wto the well done in ten minutes. its seals in all the a very thin crunchy coating which the fat does not penetrate - thereby using muchless fat than ordinary frying methods.</p>
    <p>This formula is an all -dry mix to be used on anything breaded - fish, oysters, shrimp, veal and chicken fried steak.</p>
  </div>

  <div class="abs use-heading">
    <div class="small">For</div>
    <div class="big">DEEP FAT</div>
    <div class="small">and</div>
    <div class="big">PAN FRYING</div>
    <div class="note">(SLIGHTLY LONGER ON PAN FRYING</div>
  </div>

  <div class="abs food-list">OF CHICKEN • STEAKS • CHOPS •TENDERLOING<br>• FISH • SHRIMP • OYSTERS &amp; OTHER SEA<br>FOODS •ONION RINGS &amp; VEGETABLES</div>
  <div class="abs lot-box"></div>

  <div class="abs noting-heading">NOTING<br>TO ADD</div>
  <p class="abs directions">Wet all foods in water. then place in dry dip, coating thoroughly. Fry (350° F.) chicken 1 ½ to 2# 10 minutes, over 2# slightly longer. for best reuslts double dip onion rings and oysters.</p>

  <div class="abs front-copy">
    <h2>THE ALL PURPOSE BREADING</h2>
    <p class="tag">Seals juice in - grease out</p>
    <p class="tag">Cooks two-pound chicken welldone in 10 minutes (deep fat)</p>
    <p class="slogan">Chicken fried the GOLDEN COAT way<br>is fried chicken the right way.</p>
  </div>

  <div class="abs ingredients-band">
    <p>INGREDIENTS: FLOUR, SALT, NON-FAT MILK SOLIDS, EGG YOLK,<br>BAKNG POWDER, CORN STRACH, SUGAR AND PEPPER.</p>
    <p class="net">NET WT. 10 LBS</p>
  </div>

  <div class="abs bottom-slogan">CHICKEN FRIED THE GOLDEN COAT WAY<br>IS FRIED CHICKEN THE RIGHT WAY.</div>

  <div class="abs color-bar">
    <div class="swatch-row">
      <span class="swatch"><i style="background:#fff200"></i>Yellow</span>
      <span class="swatch"><i style="background:#ec008c"></i>Magenta</span>
      <span class="swatch"><i style="background:#00aeef"></i>Cyan</span>
      <span class="swatch"><i style="background:#000"></i>Black</span>
    </div>
    <div class="swatch-row">
      <span class="swatch"><i style="background:#000"></i>Color 1</span>
      <span class="swatch"><i style="background:#000"></i>Color 2</span>
      <span class="swatch"><i style="background:#000"></i>Color 3</span>
      <span class="swatch"><i style="background:#000"></i>Color 4</span>
    </div>
    <div class="swatch-row">
      <span class="swatch"><i style="background:#7fd3f7"></i></span>
      <span class="swatch"><i style="background:#f49ac1"></i></span>
      <span class="swatch"><i style="background:#bbb"></i></span>
    </div>
    <div class="swatch-row">
      <span class="swatch"><i style="background:#fff799"></i></span>
    </div>
    <div class="swatch-row">
      <span class="swatch"><i style="background:#bde4f8"></i>Lacquer</span>
    </div>
    <span class="job-code">A-000-000-C</span>
  </div>

  <div class="abs spec">LB 7.5x4x15&nbsp; 18.5PL&nbsp; .067<br>Predistorted Flexo Template</div>
</main>
</body>
</html>
```